BBQ Grill Tongs Logo and Packaging Design

Need fun exciting logo design and packaging for the best BBQ and Grilling tongs ever used.
Company Name is
Plunko's Tongs
www.flamepincher.example
Template layout for packaging is flat 5 x 8
We want the packaging to jump off the shelf in an eye catching design that uses vibrant colors and terminology such as..
NO more sore hands
Never Slips
Lifetime Guarantee
Best for Indoor and Outdoor BBQ and Cooking
Used by the BEST BBQ Grillmasters and Cooks
Target Market(s)
outdoor and indoor cooks, all ages people who purchase bbq supplies, cooking supplies and or bbq and grilling enthusists
Industry/Entity Type
Cooking
Requirements
Must have
- Bold Branding, bright colors
Nice to have
- http://www.renlomarsk.example/
- http://www.delvatuno.example/
- http://www.humblekettleworks.example/

```html
<!DOCTYPE html>
<html lang="en">
<head>
<meta charset="utf-8">
<title>Plunko's Tongs – Packaging Panel</title>
<link rel="stylesheet" href="https://fonts.googleapis.com/css2?family=Bebas+Neue&family=Libre+Bodoni:wght@700&display=swap">
<style>
  :root {
    --ink: #000000;
    --paper: #ffffff;
    --brand-red: #e10f21;
    --shelf-yellow: #dcd91b;
    --flame-hot: #f7b12f;
    --flame-deep: #c2410f;
    --grill-dark: #3a1d10;
  }
  html, body {
    margin: 0;
    padding: 0;
    width: 1200px;
    height: 791px;
    overflow: hidden;
    background: var(--paper);
  }
  .package-panel {
    position: relative;
    width: 1200px;
    height: 791px;
    background: var(--paper);
    font-family: "Bebas Neue", "Arial Narrow", sans-serif;
  }
  .brand-block {
    position: absolute;
    left: 0; top: 0;
    width: 726px; height: 387px;
    background: var(--ink);
  }
  .brand-name {
    position: absolute;
    left: 148px; top: 52px;
    width: 392px;
    margin: 0;
    text-align: center;
    color: var(--brand-red);
    font-family: "Bebas Neue", "Arial Narrow", sans-serif;
    font-weight: 400;
    font-size: 124px;
    line-height: 112px;
    letter-spacing: 2px;
  }
  .brand-rating {
    position: absolute;
    left: 53px; top: 326px;
    margin: 0;
    color: var(--paper);
    font-family: "Libre Bodoni", "Times New Roman", serif;
    font-weight: 700;
    font-size: 31px;
    line-height: 40px;
    word-spacing: 12px;
    letter-spacing: 0.5px;
    white-space: nowrap;
  }
  .chef-block {
    position: absolute;
    left: 726px; top: 0;
    width: 474px; height: 387px;
    background: var(--brand-red);
  }
  .chef-claim {
    position: absolute;
    left: 40px; top: 82px;
    margin: 0;
    color: var(--paper);
    font-weight: 400;
    font-size: 92px;
    line-height: 76px;
    letter-spacing: 1px;
  }
  .chef-hand-art {
    position: absolute;
    right: 0; top: 83px;
    width: 245px; height: 304px;
    background: linear-gradient(160deg, rgba(0,0,0,0) 30%, rgba(0,0,0,0.55) 75%);
  }
  .benefit-block {
    position: absolute;
    left: 0; top: 404px;
    width: 495px; height: 387px;
    background: var(--shelf-yellow);
  }
  .benefit-list {
    position: absolute;
    left: 40px; top: 92px;
    margin: 0; padding: 0;
    list-style: none;
    color: var(--ink);
    font-size: 60px;
    line-height: 59px;
    letter-spacing: -0.5px;
  }
  .benefit-list li:nth-child(2) { padding-left: 5px; }
  .product-photo {
    position: absolute;
    left: 495px; top: 404px;
    width: 705px; height: 387px;
    background:
      linear-gradient(180deg, rgba(255,210,90,0.5) 0%, rgba(0,0,0,0) 30%),
      radial-gradient(ellipse at 50% 40%, var(--flame-hot) 0%, var(--flame-deep) 60%, var(--grill-dark) 100%);
  }
</style>
</head>
<body>
  <main class="package-panel">
    <section class="brand-block">
      <h1 class="brand-name">Plunko's<br>Tongs</h1>
      <p class="brand-rating">#1 RATED AMONG HOME COOKS</p>
    </section>

    <section class="chef-block">
      <h2 class="chef-claim">USED BY<br>TOP CHEFS</h2>
      <div class="chef-hand-art" role="img" aria-label="Black line illustration of a hand holding grill tongs"></div>
    </section>

    <section class="benefit-block">
      <ul class="benefit-list">
        <li>LIFE TIME GUARANTEE</li>
        <li>NO MORE SORE HANDS</li>
        <li>NEVER SLIPS</li>
      </ul>
    </section>

    <div class="product-photo" role="img" aria-label="Photo of stainless steel tongs with a wooden handle over a flaming barbecue grill"></div>
  </main>
</body>
</html>
```